Harwell Church Yuletide Recital 2013

Create a 18x22 inch poster for an upcoming church concert event with the following details:
Theme: Jesus Is Coming Again
Date:12/21/13 Time: 10:40am
Featuring the Choirs of the Harwell Church and special guests.
Harwell FGB Church
415-36 92nd Terrace,
Laurelton, NY 10987
Pastor Desmond K. Halloway
The target audience is predominantly african-american
The concert theme has been changed to: "Jesus The Light of the World"
Church

```html
<!DOCTYPE html>
<html lang="en">
<head>
<meta charset="utf-8">
<title>Jesus the Light of the World — Harwell Church</title>
<link rel="stylesheet" href="https://fonts.googleapis.com/css2?family=Audiowide&family=Archivo+Black&family=Cantarell:wght@700&display=swap">
<style>
  :root {
    --page-bg: #e9e9e9;
    --sky-deep: #4f86c9;
    --sky-mid: #8fb8e6;
    --sky-light: #d6e8f8;
    --glow: #ffffff;
    --title-rust: #b8472a;
    --date-rust: #c24a22;
    --ink: #1b2230;
  }
  * { margin: 0; padding: 0; box-sizing: border-box; }
  html, body {
    width: 900px;
    height: 1200px;
    overflow: hidden;
    background: var(--page-bg);
  }
  .poster {
    position: absolute;
    left: 0;
    top: 50px;
    width: 900px;
    height: 1100px;
    overflow: hidden;
  }
  .poster__sky {
    position: absolute;
    inset: 0;
    background:
      radial-gradient(ellipse 42% 30% at 50% 22%, var(--glow) 0%, rgba(255,255,255,0.85) 35%, rgba(255,255,255,0) 100%),
      radial-gradient(ellipse 55% 40% at 50% 60%, rgba(255,255,255,0.75) 0%, rgba(255,255,255,0) 100%),
      radial-gradient(ellipse 30% 35% at 8% 25%, rgba(255,255,255,0.6) 0%, rgba(255,255,255,0) 100%),
      radial-gradient(ellipse 30% 35% at 92% 25%, rgba(255,255,255,0.6) 0%, rgba(255,255,255,0) 100%),
      linear-gradient(180deg, var(--sky-deep) 0%, var(--sky-mid) 40%, var(--sky-light) 70%, var(--sky-mid) 100%);
  }
  .poster__title {
    position: absolute;
    left: 0;
    width: 100%;
    text-align: center;
    color: var(--title-rust);
    font-family: "Audiowide", sans-serif;
    line-height: 1;
    white-space: nowrap;
  }
  .poster__title--main {
    top: 450px;
    font-size: 180px;
    letter-spacing: 26px;
    text-indent: 26px;
  }
  .poster__title--sub {
    top: 650px;
    font-size: 52px;
    letter-spacing: 5px;
    text-indent: 5px;
  }
  .poster__datetime {
    position: absolute;
    top: 765px;
    left: 0;
    width: 100%;
    text-align: center;
    font-family: "Archivo Black", sans-serif;
    font-size: 44px;
    color: var(--date-rust);
    line-height: 1;
    white-space: nowrap;
  }
  .poster__venue {
    position: absolute;
    top: 862px;
    left: 0;
    width: 100%;
    text-align: center;
    font-family: "Cantarell", sans-serif;
    font-weight: 700;
    font-size: 22px;
    line-height: 29px;
    color: var(--ink);
    font-style: normal;
  }
  .poster__featuring {
    position: absolute;
    top: 1027px;
    left: 0;
    width: 100%;
    text-align: center;
    font-family: "Cantarell", sans-serif;
    font-weight: 700;
    font-size: 25px;
    color: var(--ink);
    line-height: 1;
    white-space: nowrap;
  }
</style>
</head>
<body>
  <main class="poster">
    <div class="poster__sky" role="img" aria-label="Background artwork: bright sky with clouds and radiant light"></div>
    <h1 class="poster__title poster__title--main">Jesus</h1>
    <p class="poster__title poster__title--sub">the Light of the World</p>
    <p class="poster__datetime">Date:12/21/13 Time: 10:40am</p>
    <address class="poster__venue">
      Harwell FGB Church<br>
      415-36 92nd Terrace,<br>
      Laurelton, NY 10987<br>
      Pastor Desmond K. Halloway
    </address>
    <p class="poster__featuring">Featuring the Choirs of the Harwell Church and special guests.</p>
  </main>
</body>
</html>
```